Seafood restaurant menu

I am looking for a new menu design for my cajun seafood restaurant. I want something modern and simple. Our menu is very small so just one page front and back. Preferred, menu size is (4.25"x11"), I have attach some images, but we will have more to give.
Updates

Need to give designer more time

Target Market(s)

young to middle aged customers

Industry/Entity Type

Restaurant Food industry

Colors
EB3D1F
EC4F4E
F09395
F8D3D4
FCEDEE

Requirements
Must have
• creativity and interesting
Nice to have
• I would like to see a clean and simple menu, but with good color placement and photos of the dishes

```html
<!DOCTYPE html>
<html lang="en">
<head>
<meta charset="utf-8">
<title>Menu Design – Marlin's Crab Shack</title>
<link rel="stylesheet" href="https://fonts.googleapis.com/css2?family=Poppins:wght@400&family=Barlow:wght@400;500;600&family=Barlow+Condensed:wght@400;500&family=Great+Vibes&display=swap">
<style>
  :root{
    --red:#EC1F27;
    --red-soft:#F09395;
    --blush:#F8D3D4;
    --mist:#FCEDEE;
    --ink:#1A1A1A;
    --muted:#444;
    --paper:#FFFFFF;
    --sea-warm:#C9764A;
    --sea-deep:#7A3A22;
  }
  *{box-sizing:border-box;margin:0;padding:0}
  html,body{width:1050px;height:1200px;overflow:hidden;background:var(--paper)}
  body{position:relative;font-family:"Barlow",sans-serif;color:var(--ink)}

  .sheet-title{position:absolute;top:54px;left:0;width:1050px;text-align:center;
    font-family:"Poppins",sans-serif;font-weight:400;font-size:40px;letter-spacing:.5px}

  .panel{position:absolute;top:161px;width:362px;height:940px;background:var(--paper);
    overflow:hidden;box-shadow:0 0 6px rgba(0,0,0,.12)}
  .panel--front{left:135px}
  .panel--back{left:555px}

  .section-head{position:absolute;z-index:2;height:23px;background:var(--red);border-radius:3px 10px 4px 9px;
    color:var(--paper);font-family:"Great Vibes",cursive;font-size:22px;line-height:25px;padding-left:13px}

  .list{position:absolute;z-index:2;font-size:13px;font-weight:500;letter-spacing:.2px}
  .row{display:flex;align-items:baseline;white-space:nowrap}
  .row .lead{flex:1;border-bottom:1px dashed var(--red);margin:0 3px;transform:translateY(-3px);min-width:8px}
  .note{position:absolute;z-index:2;font-family:"Barlow Condensed",sans-serif;font-size:8px;color:var(--muted);white-space:nowrap}
  .flavor-tag{font-family:"Barlow Condensed",sans-serif;font-size:8px;color:var(--red);font-weight:400;margin-left:4px}

  /* front */
  .front-splash{position:absolute;top:0;left:0;width:362px;height:110px}
  .brand{position:absolute;top:150px;left:0;width:362px;text-align:center;
    font-family:"Barlow",sans-serif;font-weight:600;font-size:30px;color:var(--red);line-height:36px}
  .brand-dot{display:block;width:56px;height:56px;border-radius:50%;background:var(--red);margin:0 auto 12px}
  .dish-photo{position:absolute;z-index:2;border-radius:50%;
    background:radial-gradient(circle at 45% 40%,#E7A04E 0%,var(--sea-warm) 45%,var(--sea-deep) 100%)}
  .boil-photo{position:absolute;z-index:1;left:0;top:762px;width:362px;height:178px;
    background:linear-gradient(180deg,rgba(255,255,255,1) 0%,rgba(230,190,170,.85) 16%,#C78A68 42%,#9A5438 78%,#6E3A28 100%)}

  /* back */
  .back-photo{position:absolute;left:0;top:0;width:362px;height:220px;
    background:linear-gradient(180deg,#D9CCC2 0%,#E6DCD4 55%,rgba(255,255,255,1) 100%)}
  .back-band{position:absolute;left:0;top:770px;width:362px;height:170px}
  .band-head{position:absolute;font-family:"Great Vibes",cursive;font-size:21px;color:var(--ink)}
  .band-item{position:absolute;font-size:11.5px;font-weight:500;color:var(--paper);white-space:nowrap}
  .band-sub{position:absolute;font-family:"Barlow Condensed",sans-serif;font-size:7.5px;color:var(--blush);white-space:nowrap}
  .drink-bar{position:absolute;left:83px;top:906px;width:197px;height:23px;background:var(--ink);
    border-radius:10px 4px 10px 5px;color:var(--paper);font-family:"Barlow Condensed",sans-serif;
    font-size:12px;line-height:23px;text-align:center;white-space:nowrap}
  .drink-bar small{font-size:7px;margin:0 10px 0 3px}
</style>
</head>
<body>
  <h1 class="sheet-title">Menu Design</h1>

  <!-- FRONT -->
  <section class="panel panel--front">
    <svg class="front-splash" viewBox="0 0 362 110" preserveAspectRatio="none" aria-hidden="true">
      <path d="M0 0H362V100C340 92 330 70 300 72C270 74 250 40 215 45C185 50 170 20 140 30C110 40 90 25 70 55C50 80 25 92 0 110Z" fill="var(--red)"/>
    </svg>

    <div class="brand"><span class="brand-dot"></span>Marlin's Crab Shack</div>

    <div class="section-head" style="top:288px;left:31px;width:197px">Appetizer</div>
    <div class="list" style="top:334px;left:46px;width:271px">
      <div class="row"><span>8pc. Wings</span><span class="lead"></span><span>14/8pc.</span></div>
    </div>
    <div class="note" style="top:355px;left:46px">(Honey Lemon Pepper/Buffalo/Marlin's Bomb)</div>
    <div class="list" style="top:382px;left:46px;width:271px">
      <div class="row"><span>Garlic Noodles</span><span class="lead"></span><span>7</span></div>
    </div>

    <div class="section-head" style="top:422px;left:31px;width:197px">Fried Seafood Baskets</div>
    <div class="note" style="top:456px;left:44px">(All baskets served with a side, Sweet Potato Fries or Hush Puppies +1)</div>
    <div class="list" style="top:478px;left:46px;width:148px;line-height:22px">
      <div class="row"><span>Fried Oysters</span><span class="lead"></span><span>12</span></div>
      <div class="row"><span>Fried Shrimp</span><span class="lead"></span><span>13</span></div>
      <div class="row"><span>Fried Catfish</span><span class="lead"></span><span>12</span></div>
      <div class="row"><span>Fried Calamari</span><span class="lead"></span><span>12</span></div>
      <div class="row"><span>Soft Shell Crab</span><span class="lead"></span><span>15</span></div>
    </div>
    <div class="dish-photo" role="img" aria-label="Photo of a Cajun seafood boil with shrimp and crab legs" style="left:210px;top:472px;width:132px;height:132px"></div>

    <div class="section-head" style="top:609px;left:31px;width:197px">Sides</div>
    <div class="list" style="top:643px;left:36px;width:156px;line-height:22px">
      <div class="row"><span>Cajun Fries</span><span class="lead"></span><span>5</span></div>
      <div class="row"><span>Sweet Potato Fries</span><span class="lead"></span><span>6</span></div>
      <div class="row"><span>Hush Puppies</span><span class="lead"></span><span>6</span></div>
      <div class="row"><span>Coleslaw</span><span class="lead"></span><span>4</span></div>
      <div class="row"><span>Steamed Rice</span><span class="lead"></span><span>3</span></div>
    </div>
    <div class="dish-photo" role="img" aria-label="Photo of seasoned snow crab legs arranged in a circle" style="left:222px;top:644px;width:108px;height:108px"></div>

    <div class="boil-photo" role="img" aria-label="Photo of a seafood boil tray with crab legs, lobster and corn"></div>
  </section>

  <!-- BACK -->
  <section class="panel panel--back">
    <div class="back-photo" role="img" aria-label="Faded photo of a seafood spread with lemon and herbs"></div>

    <div class="section-head" style="top:38px;left:40px;width:196px">Extras:</div>
    <div class="list" style="top:75px;left:50px;width:269px;line-height:22px">
      <div class="row"><span>Potatoes (3pc)</span><span class="lead"></span><span>$3</span></div>
      <div class="row"><span>Corn on the cob(2pc)</span><span class="lead"></span><span>$3</span></div>
      <div class="row"><span>Boiled Eggs (2pc)</span><span class="lead"></span><span>$3</span></div>
      <div class="row"><span>Sausage</span><span class="lead"></span><span>$5 ½ LB / $9 1Lb</span></div>
      <div class="row"><span>Sauce</span><span class="lead"></span><span>$6/Cup</span></div>
    </div>

    <div class="section-head" style="top:202px;left:40px;width:196px">Seafood by the LB</div>
    <div class="list" style="top:235px;left:50px;width:269px;line-height:22px">
      <div class="row"><span>Crawfish</span><span class="lead"></span><span>18</span></div>
      <div class="row"><span>Shrimp w/ head</span><span class="lead"></span><span>18</span></div>
      <div class="row"><span>Shrimp w/o head deveined</span><span class="lead"></span><span>20</span></div>
      <div class="row"><span>Clams</span><span class="lead"></span><span>18</span></div>
      <div class="row"><span>Mussels</span><span class="lead"></span><span>18</span></div>
      <div class="row"><span>Snow Crab legs</span><span class="lead"></span><span>39</span></div>
      <div class="row"><span>Lobster tail</span><span class="lead"></span><span>Seasonal</span></div>
      <div class="row"><span>King Crab Legs</span><span class="lead"></span><span>Seasonal</span></div>
    </div>

    <div class="section-head" style="top:426px;left:40px;width:196px">Seafood Plates</div>
    <div class="note" style="top:455px;left:50px">(All plates come with 1 flavor, 1 Corn, Sausages, and 1 Potato)</div>
    <div class="list" style="top:476px;left:50px;width:269px">
      <div class="row"><span>Seafood plate 2 LB<span class="flavor-tag" style="color:var(--muted)">(1 flavor)</span></span><span class="lead"></span><span>$38</span></div>
    </div>
    <div class="note" style="top:496px;left:50px">2LB Choice of Shrimp/Clams/Mussel/Crawfish</div>
    <div class="list" style="top:522px;left:50px;width:269px">
      <div class="row"><span>Snow Crab plate</span><span class="lead"></span><span>$58</span></div>
    </div>
    <div class="note" style="top:543px;left:50px">1LB Snow Crab and 1LB Choice of Shrimp/Clams/Mussel/Crawfish</div>

    <div class="section-head" style="top:582px;left:40px;width:196px">Family Meals</div>
    <div class="list" style="top:621px;left:50px;width:269px">
      <div class="row"><span>Seafood Combo 3 LB<span class="flavor-tag">(1 flavor)</span></span><span class="lead"></span><span>$60</span></div>
    </div>
    <div class="note" style="top:644px;left:50px;line-height:11px">Choice of Shrimp/Clams/Mussel/Crawfish, ½ LB Sausage,<br>2 Corns, 2 Potato, 2 Eggs, (2cups) Fountain Soda</div>
    <div class="note" style="top:671px;left:50px;color:var(--ink)">(Substitute 1LB for Snow Crab + 20)</div>
    <div class="list" style="top:692px;left:50px;width:269px">
      <div class="row"><span>Seafood Deluxe 4 LB<span class="flavor-tag">(1 flavor)</span></span><span class="lead"></span><span>$130</span></div>
    </div>
    <div class="note" style="top:715px;left:50px;line-height:11.5px">6 clusters of Snow Crab (3LB), 1LB choice of Shrimp/Clams/<br>Mussel/Crawfish, 1LB Sausage, 4 Corns, 4 Potato, 4 Eggs,<br>(2cups) Fountain Soda</div>
    <div class="note" style="top:755px;left:50px;color:var(--ink)">(Substitute 1LB for Snow Crab + 20)</div>

    <svg class="back-band" viewBox="0 0 362 170" preserveAspectRatio="none" aria-hidden="true">
      <path d="M0 20C30 30 50 5 80 12C110 20 125 0 160 8C195 16 215 2 250 10C285 18 300 0 330 6C345 9 355 2 362 0V170H0Z" fill="var(--red)"/>
    </svg>

    <div class="band-head" style="top:812px;left:40px">Choose your flavor</div>
    <div class="band-item" style="top:843px;left:40px">Cajun (classic)</div>
    <div class="band-sub" style="top:860px;left:40px">Lemon Pepper</div>
    <div class="band-item" style="top:874px;left:40px">Garlic Butter</div>
    <div class="band-sub" style="top:889px;left:40px">Marlin's Bomb</div>

    <div class="band-head" style="top:812px;left:200px">Spice it up</div>
    <div class="band-sub" style="top:844px;left:200px">Non-Spicy/Mild/Medium/Hot</div>
    <div class="band-head" style="top:857px;left:200px">Drinks</div>
    <div class="band-sub" style="top:884px;left:200px">Cola/Diet Cola/Cola Zero/Lemon-Lime</div>

    <div class="drink-bar">20oz Fountain<small>(Free Refill)</small>3</div>
  </section>
</body>
</html>
```